Harvesting Victors 6x9 book soft cover- front cover only

We need a book cover for a softcover book. We will need final files in Photoshop or InDesign is preferred.

Overall Title:
Harvesting Victors
Subtitle:
The Foundations of Humble Mentoring for Trainers, Instructors and Players
Author:
by Dr. Marcus Pettiford

The audience is high school and college coaches however we don't want the standard picture with words over the top. Make it a creative design but keep it mind it's a little academic.

```html
<!DOCTYPE html>
<html lang="en">
<head>
<meta charset="utf-8">
<title>Harvesting Victors – Front Cover</title>
<link rel="stylesheet" href="https://fonts.googleapis.com/css2?family=Antonio:wght@400;600;700&display=swap">
<style>
  :root {
    --cover-red: #a8291b;
    --sun-gold: #ecc262;
    --title-gold: #e6a52a;
    --peach: #f3cba4;
    --figure-blue: #3f5a6e;
    --figure-orange: #d9822f;
  }
  html, body {
    margin: 0;
    padding: 0;
    width: 833px;
    height: 1200px;
    overflow: hidden;
    background: var(--cover-red);
  }
  .cover {
    position: relative;
    width: 833px;
    height: 1200px;
    background: var(--cover-red);
  }
  .cover-art {
    position: absolute;
    inset: 0;
    width: 833px;
    height: 1200px;
  }
  .type {
    font-family: "Antonio", "Oswald", sans-serif;
  }
  .subtitle { fill: var(--peach); font-weight: 400; font-size: 44px; }
  .title-top { fill: var(--peach); font-weight: 600; font-size: 86px; }
  .title-main { fill: var(--title-gold); font-weight: 700; font-size: 190px; }
  .author { fill: var(--peach); font-weight: 600; font-size: 46px; }
</style>
</head>
<body>
<main class="cover">
  <svg class="cover-art" viewBox="0 0 833 1200" xmlns="http://www.w3.org/2000/svg">
    <defs>
      <clipPath id="sun-clip">
        <path d="M0 0 H833 V760 Q416 688 0 760 Z"/>
      </clipPath>
      <linearGradient id="figure-tones" x1="0" y1="0" x2="1" y2="0">
        <stop offset="0" stop-color="var(--figure-blue)"/>
        <stop offset="0.55" stop-color="#5b6a74"/>
        <stop offset="1" stop-color="var(--figure-orange)"/>
      </linearGradient>
    </defs>

    <rect class="background" width="833" height="1200" fill="var(--cover-red)"/>

    <!-- Subtitle -->
    <g class="type">
      <text class="subtitle" x="417" y="104" text-anchor="middle" textLength="614" lengthAdjust="spacingAndGlyphs">The Foundations of Humble Mentoring for</text>
      <text class="subtitle" x="417" y="162" text-anchor="middle" textLength="516" lengthAdjust="spacingAndGlyphs">Trainers, Instructors and Players</text>
    </g>

    <!-- Sun disc -->
    <g class="sun" clip-path="url(#sun-clip)">
      <circle cx="416" cy="560" r="292" fill="var(--sun-gold)"/>
    </g>

    <!-- Illustration area: coach and student -->
    <rect class="illustration" role="img"
          aria-label="Illustration: a bespectacled coach in a patchwork suit holding a gold trophy beside a young student with a backpack"
          x="190" y="205" width="460" height="505" rx="24"
          fill="url(#figure-tones)" opacity="0.85"/>

    <!-- Swoosh -->
    <path class="swoosh" d="M120 762 Q416 668 712 762 Q416 694 120 762 Z" fill="var(--sun-gold)"/>

    <!-- Title -->
    <g class="type">
      <text class="title-top" x="418" y="830" text-anchor="middle" textLength="340" lengthAdjust="spacingAndGlyphs">HARVESTING</text>
      <text class="title-main" x="418" y="1005" text-anchor="middle" textLength="540" lengthAdjust="spacingAndGlyphs">VICTORS</text>
      <text class="author" x="418" y="1128" text-anchor="middle" textLength="620" lengthAdjust="spacing" letter-spacing="8">BY DR. MARCUS PETTIFORD</text>
    </g>
  </svg>
</main>
</body>
</html>
```